Redesign of an educational Eye website for Medical Students and Healthcare professionals

www.corvantisportal.com is an educational resource, illustrated using high quality 3D animations, for undergraduate medical students and healthcare professionals to learn about the anatomy of the human eye and associated common eye disorders.

The website was originally developed (using a Joomla template) a couple of years ago and we now want to update the brand and design of the site. Example content and animations can be found at https://www.corvantisportal.com/overview or https://www.corvantisportal.com/ocular-anatomy/orbital-anatomy

We would like a new logo and home page design (to include new colour palette, fonts and updated overall design).

The attached PowerPoint contains an example layout of the revised components we want to appear on the new Home page. We plan to have a hero panel at the top of page playing a short video of some of the animations. Similar to how this site works (www.zembri.uk.com).

We want the new site to feel Professional, Modern and Clean and simple.

Target Market(s)

Undergraduate medical students and Healthcare Professionals

Industry/Entity Type

Medical

Logo Text

Corvantis Portal

Number of Pages Required

1 page

Font styles to use
Sans Serif

Colors

Designer to choose colors to be used in the design.

```html
<!DOCTYPE html>
<html lang="en">
<head>
<meta charset="utf-8">
<title>Corvantis Portal — Training Modules</title>
<link href="https://fonts.googleapis.com/css2?family=Jost:wght@300;400;500&display=swap" rel="stylesheet">
<style>
:root{
  --accent:#1f6f8b;
  --light-bg:#f1f1f1;
  --card-bg:#ffffff;
  --card-border:#dcdcdc;
  --ink:#333333;
  --ink-soft:#444444;
  --muted:#6a6a6a;
  --dark-bg:#333333;
  --white:#ffffff;
}
*{box-sizing:border-box;margin:0;padding:0}
html,body{width:1200px;height:749px;overflow:hidden;font-family:"Jost",sans-serif;color:var(--ink)}
.page{position:relative;width:1200px;height:749px;overflow:hidden}
.modules{position:absolute;top:0;left:0;width:1200px;height:434px;background:var(--light-bg);border-top:2px solid var(--accent)}
.section-title{position:absolute;left:0;width:100%;text-align:center;font-weight:400;font-size:24px;letter-spacing:-.3px}
.modules .section-title{top:24px;color:var(--ink)}
.card{position:absolute;top:93px;width:267px;height:313px;background:var(--card-bg);border:1px solid var(--card-border);text-align:center}
.card-1{left:181px}.card-2{left:471px}.card-3{left:761px}
.card-icon{position:absolute;top:22px;left:50%;transform:translateX(-50%);width:110px;height:110px}
.card-title{position:absolute;top:146px;left:0;width:100%;font-weight:400;font-size:21px;line-height:21px;font-variant:small-caps;color:var(--ink)}
.card-text{position:absolute;left:0;width:100%;font-weight:300;font-size:14.5px;line-height:20px;color:var(--ink-soft)}
.card-1 .card-text{top:201px}.card-2 .card-text{top:200px}.card-3 .card-text{top:200px}
.card-link{position:absolute;left:0;width:100%;font-size:11.5px;letter-spacing:1.6px;color:var(--muted);font-weight:400}
.card-1 .card-link{top:278px}.card-2 .card-link{top:277px}.card-3 .card-link{top:274px}
.team{position:absolute;top:434px;left:0;width:1200px;height:315px;background:var(--dark-bg)}
.team .section-title{top:24px;color:var(--white)}
.team-row{position:absolute;top:104px;left:149px;display:flex}
.member{position:relative;width:228px;height:215px;border-right:1px solid #555}
.member:last-child{border-right:none}
.photo{position:absolute;inset:0}
.photo-1{background:linear-gradient(180deg,#b9a79b 0%,#e4ddd8 60%,#cfd3da 100%)}
.photo-2{background:linear-gradient(160deg,#dfe5ea 0%,#d5b39d 55%,#3f4a4f 100%)}
.photo-3{background:linear-gradient(180deg,#ffffff 0%,#c9a288 45%,#8d8273 100%)}
.photo-4{background:linear-gradient(180deg,#ffffff 0%,#e7cfa5 40%,#f1efec 100%)}
.overlay{position:absolute;inset:0;background:rgba(128,128,128,.88);text-align:center;color:var(--white)}
.member-name{margin-top:46px;font-size:19px;font-weight:400;letter-spacing:-.2px;text-transform:uppercase}
.member-bio{margin:10px auto 0;width:200px;font-size:10.5px;line-height:19px;font-weight:300}
</style>
</head>
<body>
<div class="page">
  <section class="modules">
    <h2 class="section-title">TRAINING MODULES</h2>

    <article class="card card-1">
      <svg class="card-icon" viewBox="0 0 110 110" aria-hidden="true">
        <circle cx="55" cy="55" r="50" fill="none" stroke="#333" stroke-width="5"/>
        <polygon points="30,32 60,50 80,79 50,60" fill="#333"/>
        <polygon points="40,41 55,50 50,56" fill="#fff"/>
      </svg>
      <h3 class="card-title">Core Principles</h3>
      <p class="card-text">Diagnostic, deep dive and<br>pulse surveys with powerful analytics<br>and action planning.</p>
      <a class="card-link">LEARN&nbsp; MORE</a>
    </article>

    <article class="card card-2">
      <svg class="card-icon" viewBox="0 0 110 110" aria-hidden="true">
        <circle cx="84" cy="14" r="10" fill="#333"/>
        <g fill="none" stroke="#333" stroke-width="11" stroke-linecap="round" stroke-linejoin="round">
          <path d="M72 32 L58 62"/>
          <path d="M72 32 L52 30 L42 44"/>
          <path d="M72 32 L80 44 L92 36"/>
          <path d="M58 62 L74 74 L66 100"/>
          <path d="M58 62 L44 82 L18 82"/>
        </g>
      </svg>
      <h3 class="card-title">Ophtalmology in<br>Practice</h3>
      <p class="card-text">Automated Employee Surveys<br>for each milestone:<br>candidaate, onboarding, exit and more.</p>
      <a class="card-link">LEARN&nbsp; MORE</a>
    </article>

    <article class="card card-3">
      <svg class="card-icon" viewBox="0 0 110 110" aria-hidden="true">
        <g fill="#333">
          <circle cx="18" cy="14" r="10"/><circle cx="92" cy="14" r="10"/><circle cx="55" cy="22" r="11"/>
          <rect x="5" y="28" width="26" height="44" rx="6"/><rect x="79" y="28" width="26" height="44" rx="6"/>
          <rect x="10" y="60" width="16" height="30" rx="4"/><rect x="84" y="60" width="16" height="30" rx="4"/>
          <rect x="38" y="37" width="34" height="48" rx="7" stroke="#fff" stroke-width="3"/>
          <rect x="45" y="70" width="20" height="38" rx="5"/>
        </g>
      </svg>
      <h3 class="card-title">An Other</h3>
      <p class="card-text">Action-oriented 180º and 360º<br>feedback for managers,<br>individuals and teams.</p>
      <a class="card-link">LEARN&nbsp; MORE</a>
    </article>
  </section>

  <section class="team">
    <h2 class="section-title">MEET THE TEAM</h2>
    <div class="team-row">
      <div class="member">
        <div class="photo photo-1" role="img" aria-label="Portrait photo of a female doctor with a stethoscope"></div>
        <div class="overlay">
          <h3 class="member-name">Marisol Kettering</h3>
          <p class="member-bio">Lorem ipsum dolor sit amet, consectetur adipiscing elit. Aliquam eu est ullamcorper, feugiat mauris vitae, elementum eros. Sus-pendisse pharetra tortor augue, eget pre-tium felis suscipit sit amet.</p>
        </div>
      </div>
      <div class="member"><div class="photo photo-2" role="img" aria-label="Portrait photo of a young male doctor in a clinic"></div></div>
      <div class="member"><div class="photo photo-3" role="img" aria-label="Portrait photo of a smiling man in a grey suit with arms crossed"></div></div>
      <div class="member"><div class="photo photo-4" role="img" aria-label="Portrait photo of a smiling woman in glasses and a white jacket"></div></div>
    </div>
  </section>
</div>
</body>
</html>
```